IT Professional Services Marketing Web Site

The Kovrel Associates new web site, need to look clean and modern, it has to give the feel of a professional IT consulting firm (something like white / clean background), the design need to be influenced by this site: http://www.trundavio.com/ .
The whole site is a one page, plus a link to a blog site, with the following sections:
1. Menu
2. Main Area
3. Our Company
4. What we do
5. Our Clients
6. Our People
7. Events
8. Contact Us
The new web site will be hosted on WordPress
Updates

Target Market(s)

Project Management Offices in Medium to Large Organisations

Industry/Entity Type

It Company

Number of Pages Required

1 page

Font styles to use
Serif
Sans Serif

Requirements
Must have
• Implemented on WordPress
Nice to have
• Shadows on the images and areas to give the site a bit of depth

```html
<!DOCTYPE html>
<html lang="en">
<head>
<meta charset="utf-8">
<title>Kovrel Associates — Trusted PMO Partners</title>
<link href="https://fonts.googleapis.com/css2?family=Mulish:wght@300;400;600;700;800&display=swap" rel="stylesheet">
<style>
:root{
  --cyan:#1fb1e6;
  --cyan-dark:#0f8fc2;
  --orange:#f7821b;
  --grey:#c7c7c7;
  --grey-light:#f1f1f1;
  --text:#555;
  --heading:#333;
  --navy:#0f3a57;
  --footer:#2d2d2d;
  --footer-bottom:#232323;
  --white:#fff;
}
*{box-sizing:border-box;margin:0;padding:0}
html,body{width:1200px;height:4534px;overflow:hidden}
body{font-family:"Mulish",Arial,sans-serif;color:var(--text);background:var(--white);font-size:13px;line-height:1.55}
.section-title{text-align:center;font-size:24px;font-weight:600;color:var(--heading);letter-spacing:1px;text-transform:uppercase}
.ph{display:block}

/* header */
.site-header{height:90px;display:flex;align-items:center;justify-content:space-between;padding:0 70px;background:var(--white)}
.brand{display:flex;align-items:center;gap:10px;font-size:26px;font-weight:700;color:var(--navy)}
.brand-dot{width:22px;height:22px;border-radius:50%;background:var(--orange)}
.main-nav{display:flex;gap:28px;font-size:14px;color:var(--heading)}

/* hero */
.hero{height:470px;background:linear-gradient(#efefef,#e2e2e2);position:relative;padding:110px 0 0 70px}
.hero h1{font-size:66px;font-weight:300;color:#555;line-height:1.02}
.hero h1 .accent{color:var(--orange)}
.hero-sub{font-size:22px;color:var(--cyan);margin-top:12px;line-height:1.3;width:430px}
.hero-art{position:absolute;right:80px;top:20px;width:610px;height:420px;border-radius:50%;background:radial-gradient(circle,#f6f6f6 0%,#d9d9d9 100%)}
.hero-dots{position:absolute;left:70px;bottom:20px;display:flex;gap:8px}
.hero-dots span{width:11px;height:11px;border-radius:50%;background:#aaa}
.hero-dots span:first-child{background:#555}

/* intro */
.intro{height:345px;padding:30px 230px 0 160px;font-size:13.5px}
.intro .lead{color:var(--cyan-dark);font-weight:600;margin-bottom:20px}
.intro p{margin-bottom:18px}

/* services */
.services{height:985px;background:var(--grey-light);padding-top:60px;box-shadow:inset 0 8px 10px -8px rgba(0,0,0,.2)}
.service{position:relative;height:280px;padding:0 75px}
.service h3{font-size:22px;font-weight:400;text-transform:uppercase;margin-bottom:8px}
.service p{width:490px;font-size:13px}
.service-cloud h3{color:var(--cyan)}
.service-consult h3{color:#777}
.service-care h3{color:var(--orange)}
.service-cloud{margin-top:50px}
.service-cloud .txt{padding-top:35px}
.service-cloud .art{position:absolute;right:80px;top:-10px;width:500px;height:240px;border-radius:120px;background:linear-gradient(#ffffff,#e4eef5)}
.service-consult .txt{position:absolute;left:540px;top:40px}
.service-consult .art{position:absolute;left:80px;top:0;width:390px;height:230px;background:linear-gradient(#5f8dc8,#c9d6e4)}
.service-care .art{position:absolute;right:160px;top:50px;width:250px;height:200px;background:linear-gradient(#dcdcdc,#9b9b9b)}

/* what we do */
.what{height:520px;padding-top:45px}
.tabs{display:flex;margin:42px 75px 0;height:120px}
.tab{flex:1;display:flex;align-items:center;justify-content:center;gap:22px;color:var(--white);font-size:22px;text-transform:uppercase}
.tab-cloud{background:var(--cyan)}
.tab-consult{background:var(--grey)}
.tab-care{background:var(--orange)}
.tab svg{width:70px;height:70px}
.what-panel{height:300px;background:var(--cyan);color:var(--white);position:relative;padding:42px 0 0 425px}
.what-panel h3{font-size:22px;font-weight:400;margin-bottom:10px}
.what-panel p{width:680px;font-size:13px;color:#e8f7fd}
.what-panel .panel-art{position:absolute;left:90px;top:60px;width:250px;height:180px;border-radius:12px;background:linear-gradient(#4cc2ec,#1a9fd2)}
.btn-row{display:flex;gap:18px;margin-top:22px}
.btn{background:var(--navy);color:var(--white);font-size:12px;padding:9px 22px;text-transform:uppercase}

/* clients */
.clients{height:410px;padding-top:30px}
.clients .sub{text-align:center;font-size:26px;color:#777;margin-top:4px}
.client-grid{position:relative;margin:25px 75px 0;height:260px}
.tile{position:absolute;font-size:11px;padding:10px;color:var(--white)}
.tile.big{font-size:17px;line-height:1.3}

/* people */
.people{height:435px;padding-top:60px}
.people-row{display:flex;justify-content:space-between;padding:0 90px;margin-top:50px}
.person{width:210px;text-align:center}
.person .photo{width:100px;height:100px;margin:0 auto 14px;border-radius:50%;background:linear-gradient(#cfd6dd,#8e99a3)}
.person h4{font-size:14px;color:var(--heading);font-weight:700}
.person .role{font-size:12px;color:#888;margin-bottom:8px}
.person p{font-size:12.5px}
.people-dots{display:flex;justify-content:center;gap:8px;margin-top:40px}
.people-dots span{width:11px;height:11px;border-radius:50%;background:#888}
.people-dots span:first-child{background:var(--cyan)}

/* contact */
.contact{height:515px;position:relative;background:linear-gradient(135deg,#6c7561,#4f5a4c 60%,#5c6658)}
.contact .section-title{color:var(--white);padding-top:35px}
.contact-boxes{position:absolute;left:340px;top:90px;display:flex;gap:12px}
.offices{width:245px;height:390px;background:var(--orange);color:var(--white);padding:0 16px}
.box-head{font-size:19px;text-transform:uppercase;text-align:center;padding:8px 0;border-bottom:1px solid rgba(255,255,255,.6);margin-bottom:10px}
.office{text-align:center;font-size:11px;margin-bottom:18px;line-height:1.45}
.office strong{font-size:13px;display:block}
.quick{width:245px;height:390px;background:var(--orange);padding:0 18px;color:var(--white)}
.field{background:var(--white);height:32px;margin-bottom:10px;font-size:12px;color:#999;text-align:center;line-height:32px}
.field.msg{height:205px}
.submit{background:var(--footer);color:var(--white);text-align:center;font-size:13px;padding:8px 0;text-transform:uppercase}

/* events */
.events{height:315px;padding-top:40px}
.event-row{display:flex;justify-content:space-between;padding:0 75px;margin-top:30px}
.event{width:300px}
.event h4{font-size:15px;color:var(--heading);font-weight:700}
.event .date{font-size:12px;color:#888}
.event h3{width:270px;font-size:28px;font-weight:400;color:var(--cyan);line-height:1.2;margin:6px 0 18px}
.rsvp{display:inline-block;border:1px solid #999;padding:6px 28px;font-size:11px;color:#555}

/* newsletter */
.newsletter{margin:0 75px;height:115px;border:1px solid #bbb;display:flex;align-items:center;padding:0 30px;gap:40px}
.newsletter h3{font-size:22px;font-weight:400;color:var(--heading);text-transform:uppercase;white-space:nowrap}
.newsletter .email{flex:1;height:40px;border-bottom:1px solid #ddd;color:#aaa;font-size:13px;line-height:40px}
.newsletter .subscribe{background:var(--footer);color:var(--white);padding:11px 30px;font-size:13px;text-transform:uppercase}

/* footer */
.site-footer{position:absolute;top:4240px;left:0;width:1200px;height:210px;background:var(--footer);display:flex;padding:30px 75px 0;color:#ddd}
.foot-col{width:175px}
.foot-col h5{font-size:16px;color:var(--white);font-weight:600;margin-bottom:14px}
.foot-col li{list-style:none;font-size:11px;color:#aaa;margin-bottom:6px}
.foot-col .stack li{font-size:15px;color:var(--white);margin-bottom:18px}
.social{display:flex;gap:6px}
.social span{width:22px;height:22px;border-radius:50%;background:#ddd}
.footer-bottom{position:absolute;top:4450px;left:0;width:1200px;height:84px;background:var(--footer-bottom);display:flex;align-items:center;gap:20px;padding:0 75px;color:#888;font-size:10px}
.footer-bottom .brand{font-size:16px;color:#ccc}
</style>
</head>
<body>

<header class="site-header">
  <div class="brand">Kovrel Associates <span class="brand-dot"></span></div>
  <nav class="main-nav">
    <span>Our Company</span><span>What we do</span><span>Our Clients</span><span>Our People</span><span>Events</span><span>Blog</span><span>Contact Us</span>
  </nav>
</header>

<section class="hero">
  <h1>Trusted <span class="accent">PMO</span><br>Partners.</h1>
  <p class="hero-sub">Smart Project PortfolioManagement Tools Powered by Velantic..</p>
  <div class="hero-art" role="img" aria-label="Word cloud of portfolio terms such as Tasks, Risks, Issues, Workflow and Timesheets, ringed by small icons for money, time, documents and reports"></div>
  <div class="hero-dots"><span></span><span></span><span></span><span></span></div>
</section>

<section class="intro">
  <p class="lead">"Kovrel Associates is a specialist consulting company that focuses solely on the design, configuration, deployment, user training and support of Enterprise Project Management (EPM) solutions based upon Velantic Portfolio Server and its supporting technologies. Kovrel Associates offers a true, end-to-end set of services for any organisation implementing an EPM solution within their business – to cover the lifecycle of that system.</p>
  <p>This 100% focus on Velantic EPM systems means that the company has an in-depth of knowledge and experience that is unique in the Australian marketplace. Whether it's a complete implementation project, a hosted solution option, or on-going support for an existing system, Kovrel Associates have the services to meet its customers' needs.</p>
  <p>The team come from a diverse range of backgrounds including Engineering (Civil, Chemical and Systems), Project Management, and Software Development. A number have worked with Velantic and Velantic Consulting Services directly. Kovrel Associates continues to work closely with Velantic to ensure awareness of latest product developments"</p>
</section>

<section class="services">
  <h2 class="section-title">Our Services</h2>
  <div class="service service-cloud">
    <div class="txt">
      <h3>Cloud</h3>
      <p>Aliquam molestie, mi et imperdiet euismod, dui purus auctor tellus, et interdum lacus lectus et ante. Sed accumsan sollicitudin sapien, sit amet adipiscing turpis gravida ac. In congue, neque ac lobortis volutpat, libero mauris varius mi, vitae suscipit ipsum ligula vitae risus. Duis aliquam nibh a dui iaculisemenus id a velit. Vivamus egestas risus in magna varius commodo. Sed semper viverra egestas. Etiam pretium porttitor lectus, vel ornare neque porta volutpat.</p>
    </div>
    <div class="art" role="img" aria-label="Cloud containing two open boxes with on-premise and hosted platform badges"></div>
  </div>
  <div class="service service-consult">
    <div class="art" role="img" aria-label="Office towers beside two business people"></div>
    <div class="txt">
      <h3>Consult</h3>
      <p>Aliquam molestie, mi et imperdiet euismod, dui purus auctor tellus, et interdum lacus lectus et ante. Sed accumsan sollicitudin sapien, sit amet adipiscing turpis gravida ac. In congue, neque ac lobortis volutpat, libero mauris varius mi, vitae suscipit ipsum ligula vitae risus. Duis aliquam nibh a dui iaculisemenus id a velit. Vivamus egestas risus in magna varius commodo. Sed semper viverra egestas. Etiam pretium porttitor lectus, vel ornare neque porta volutpat.</p>
    </div>
  </div>
  <div class="service service-care">
    <div class="txt">
      <h3>Care</h3>
      <p>Aliquam molestie, mi et imperdiet euismod, dui purus auctor tellus, et interdum lacus lectus et ante. Sed accumsan sollicitudin sapien, sit amet adipiscing turpis gravida ac. In congue, neque ac lobortis volutpat, libero mauris varius mi, vitae suscipit ipsum ligula vitae risus. Duis aliquam nibh a dui iaculisemenus id a velit. Vivamus egestas risus in magna varius commodo. Sed semper viverra egestas. Etiam pretium porttitor lectus, vel ornare neque porta volutpat.</p>
    </div>
    <div class="art" role="img" aria-label="Support agent with headset at a laptop"></div>
  </div>
</section>

<section class="what">
  <h2 class="section-title">What we do</h2>
  <div class="tabs">
    <div class="tab tab-cloud">
      <svg viewBox="0 0 70 70" fill="none" stroke="#fff" stroke-width="2.5"><circle cx="35" cy="35" r="32"/><path d="M22 42h26a8 8 0 0 0 0-16 11 11 0 0 0-21-2 8 8 0 0 0-5 18z"/></svg>Cloud
    </div>
    <div class="tab tab-consult">
      <svg viewBox="0 0 70 70" fill="none" stroke="#fff" stroke-width="2.5"><circle cx="35" cy="35" r="32"/><circle cx="27" cy="28" r="5"/><circle cx="43" cy="28" r="5"/><path d="M18 46c0-7 5-10 9-10s9 3 9 10M34 46c0-7 5-10 9-10s9 3 9 10"/></svg>Consult
    </div>
    <div class="tab tab-care">
      <svg viewBox="0 0 70 70" fill="none" stroke="#fff" stroke-width="2.5"><circle cx="35" cy="35" r="32"/><circle cx="35" cy="26" r="6"/><path d="M20 46c4-3 8-4 12-3l8 2c3 1 3 4 0 4h-8M20 46l10 6 18-6"/></svg>Care
    </div>
  </div>
  <div class="what-panel">
    <div class="panel-art" role="img" aria-label="Outline illustration of a cloud with gears"></div>
    <h3>Fully Customizeable, Fully Flaxable</h3>
    <p>Aliquam molestie, mi et imperdiet euismod, dui purus auctor tellus, et interdum lacus lectus et ante. Sed accumsan sollicitudin sapien, sit amet adipiscing turpis gravida ac. In congue, neque ac lobortis volutpat, libero mauris varius mi, vitae suscipit ipsum ligula vitae risus. Duis aliquam nibh a dui iaculisemenus id a velit. Vivamus egestas risus in magna varius commodo. Sed semper viverra egestas. Etiam pretium porttitor lectus, vel ornare neque porta volutpat.</p>
    <div class="btn-row"><span class="btn">Get it now</span><span class="btn">Contact us</span></div>
  </div>
</section>

<section class="clients">
  <h2 class="section-title">Our Clients</h2>
  <p class="sub">Pmo Accross Australia Share the Love</p>
  <div class="client-grid">
    <div class="ph" role="img" aria-label="Hand touching a cloud network graphic" style="position:absolute;left:0;top:0;width:220px;height:185px;background:linear-gradient(#2a3640,#5b6a78)"></div>
    <div class="tile big" style="left:0;top:185px;width:220px;height:75px;background:var(--cyan)">Vestibulum ante ipsum primis in foucibus orci</div>
    <div class="tile" style="left:225px;top:0;width:112px;height:125px;background:var(--orange)">Vestibulum ante ipsum primis in foucibus orci lectus.</div>
    <div class="tile" style="left:225px;top:130px;width:112px;height:125px;background:var(--orange)">Vestibulum ante ipsum primis in foucibus orci lectus.</div>
    <div class="tile" style="left:342px;top:0;width:235px;height:125px;background:var(--orange)">Vivamus egestas risus in magna varius commodo. Sed semper viverra egestas. Etiam pretium porttitor lectus.</div>
    <div class="ph" role="img" aria-label="Business team at a table" style="position:absolute;left:342px;top:130px;width:112px;height:125px;background:linear-gradient(#8b8f95,#4a4f57)"></div>
    <div class="tile" style="left:459px;top:130px;width:118px;height:125px;background:#d9d9d9;color:#555">Vestibulum ante ipsum primis in foucibus orci lectus.</div>
    <div class="ph" role="img" aria-label="Business people meeting" style="position:absolute;left:582px;top:0;width:112px;height:125px;background:linear-gradient(#a9aeb3,#6c7279)"></div>
    <div class="tile" style="left:582px;top:130px;width:235px;height:125px;background:var(--cyan)">Vivamus egestas risus in magna varius commodo. Sed semper viverra egestas. Etiam pretium porttitor lectus.</div>
    <div class="tile" style="left:699px;top:0;width:118px;height:125px;background:#d9d9d9;color:#555">Vestibulum ante ipsum primis in foucibus orci lectus.</div>
    <div class="ph" role="img" aria-label="Illustrated office worker in front of a city skyline" style="position:absolute;left:822px;top:0;width:228px;height:185px;background:linear-gradient(#cfe3ef,#f2f2f2)"></div>
    <div class="tile big" style="left:822px;top:185px;width:228px;height:75px;background:var(--orange)">Vestibulum ante ipsum primis in foucibus orci</div>
  </div>
</section>

<section class="people">
  <h2 class="section-title">Our People</h2>
  <div class="people-row">
    <div class="person"><div class="photo" role="img" aria-label="Portrait of a team member"></div><h4>NAME HEADING</h4><div class="role">President CEO</div><p>Aliquam molestie, mi et imperdiet euismod, dui purus auctor tellus, et interdum lacus lectus et ante.</p></div>
    <div class="person"><div class="photo" role="img" aria-label="Portrait of a team member"></div><h4>NAME HEADING</h4><div class="role">President CEO</div><p>Aliquam molestie, mi et imperdiet euismod, dui purus auctor tellus, et interdum lacus lectus et ante.</p></div>
    <div class="person"><div class="photo" role="img" aria-label="Portrait of a team member"></div><h4>NAME HEADING</h4><div class="role">President CEO</div><p>Aliquam molestie, mi et imperdiet euismod, dui purus auctor tellus, et interdum lacus lectus et ante.</p></div>
    <div class="person"><div class="photo" role="img" aria-label="Portrait of a team member"></div><h4>NAME HEADING</h4><div class="role">President CEO</div><p>Aliquam molestie, mi et imperdiet euismod, dui purus auctor tellus, et interdum lacus lectus et ante.</p></div>
  </div>
  <div class="people-dots"><span></span><span></span><span></span></div>
</section>

<section class="contact" role="img" aria-label="Map background of the region around the head office">
  <h2 class="section-title">Contact Us</h2>
  <div class="contact-boxes">
    <div class="offices">
      <div class="box-head">Offices</div>
      <div class="office"><strong>Kovrel Head Office</strong>Level 4, 18 Marlow Street<br>Brindale QLD 4821<br>Phone: 07 5550 1842<br>Fax: 07 5550 1843</div>
      <div class="office"><strong>Kovrel Head Office</strong>Level 4, 18 Marlow Street<br>Brindale QLD 4821<br>Phone: 07 5550 1842<br>Fax: 07 5550 1843</div>
      <div class="office"><strong>Kovrel Head Office</strong>Level 4, 18 Marlow Street<br>Brindale QLD 4821<br>Phone: 07 5550 1842<br>Fax: 07 5550 1843</div>
    </div>
    <div class="quick">
      <div class="box-head">Quick Contact</div>
      <div class="field">Name</div>
      <div class="field">Email Address</div>
      <div class="field msg">Message</div>
      <div class="submit">Submit Now</div>
    </div>
  </div>
</section>

<section class="events">
  <h2 class="section-title">Events Section</h2>
  <div class="event-row">
    <div class="event"><h4>Next Kovrel Events:</h4><div class="date">March 18, 2015 – 5:45pm</div><h3>Lorem ipsum dolor sit amet</h3><span class="rsvp">RSVP</span></div>
    <div class="event"><h4>Next Kovrel Events:</h4><div class="date">March 18, 2015 – 5:45pm</div><h3>Lorem ipsum dolor sit amet</h3><span class="rsvp">RSVP</span></div>
    <div class="event"><h4>Next Kovrel Events:</h4><div class="date">March 18, 2015 – 5:45pm</div><h3>Lorem ipsum dolor sit amet</h3><span class="rsvp">RSVP</span></div>
  </div>
</section>

<section class="newsletter">
  <h3>Subscribe to our newsletter</h3>
  <div class="email">Enter Email Address</div>
  <span class="subscribe">Subscribe</span>
</section>

<footer class="site-footer">
  <div class="foot-col"><h5>About</h5><ul><li>About Kovrel</li><li>Industry Recognition</li><li>Partners</li><li>Meet the team</li><li>Contact</li></ul></div>
  <div class="foot-col"><h5>Contact</h5><h5>Support</h5><ul><li>Contact support</li></ul></div>
  <div class="foot-col"><h5>Blog</h5><h5>Customers</h5></div>
  <div class="foot-col"><ul class="stack"><li>Packages</li><li>Schemes</li><li>Services</li><li>Cloud</li></ul></div>
  <div class="foot-col"><h5>Connect Us</h5><div class="social"><span></span><span></span><span></span><span></span><span></span><span></span><span></span></div></div>
</footer>
<div class="footer-bottom"><span class="brand">Kovrel</span><span>Copyright © 2015 Kovrel Associates.<br>All Right Reserved</span></div>

</body>
</html>
```